1 Page Sales Brochure of our Services

I need to create a one page brochure that our sales team can take into meetings about our services - Need this to be an impressive one page that looks fresh and new using our brand colors of Brindle green, black and white. Our brand looks "clean" think Marlo brand in how everything is clean and white and crisp. Our website showcases our services: https://brindlesports.example/services/ --- After done with this project I would like to create a full booklet. Want to begin with this project first.

Target Market(s)

State of Texas

Industry/Entity Type

Sports Construction in Texas Only

Font styles to use
Serif

Colors
00AB8E
00BBA5
67D7C9
C6EFE9
E9F9F6

Requirements
Must have
• Front and Back and cover our services outlined on our website: https://brindlesports.example/services/
Nice to have
• Need one that can get sent digital and printed -- Our colors are the Brindle green, white and black - We want brochure to look clean, almost like the Marlo feel of their product's branding

```html
<!DOCTYPE html>
<html lang="en">
<head>
<meta charset="utf-8">
<title>Brindle Sports Construction – Services Brochure</title>
<link href="https://fonts.googleapis.com/css2?family=Bebas+Neue&family=Montserrat:wght@400;500;600&display=swap" rel="stylesheet">
<style>
:root{
  --brand-green:#17703a;
  --brand-green-line:#6fb07f;
  --card-bg:#f3f7f0;
  --ink:#1d1d1d;
  --body-ink:#333;
  --paper:#ffffff;
  --backdrop:#c6d4d3;
  --dark-panel:#2a2a2a;
}
*{box-sizing:border-box;margin:0;padding:0}
html,body{width:1200px;height:798px;overflow:hidden}
body{background:var(--backdrop);position:relative;font-family:"Montserrat",sans-serif;color:var(--body-ink)}
.page{position:absolute;background:var(--paper);overflow:hidden}
.page--front{left:39px;top:51px;width:539px;height:693px}
.page--back{left:614px;top:52px;width:537px;height:691px}

.hero{position:absolute;left:0;top:0;width:100%;height:246px;
  background:linear-gradient(160deg,#b8a88c 0%,#cfc3ac 35%,#a9a59d 60%,#8f8e88 100%)}
.brand-box{position:absolute;left:19px;top:0;width:156px;height:85px;background:var(--paper);
  border-radius:0 0 8px 8px;display:flex;flex-direction:column;align-items:center;justify-content:center}
.brand-name{font-family:"Bebas Neue",sans-serif;font-size:40px;line-height:1;color:var(--brand-green);letter-spacing:1px}
.brand-tag{font-size:8px;font-weight:600;color:var(--brand-green);margin-top:2px}

.intro{position:absolute;left:19px;top:183px;width:500px;height:130px;background:var(--brand-green);
  border-radius:8px;display:flex;align-items:center;color:#fff}
.intro-title{font-family:"Bebas Neue",sans-serif;font-weight:400;font-size:24px;line-height:24.5px;width:151px;padding-left:21px;letter-spacing:.5px}
.intro-rule{width:1px;height:92px;background:rgba(255,255,255,.6)}
.intro-copy{flex:1;padding:0 20px 0 22px;font-size:7px;line-height:12px}
.intro-copy p+p{margin-top:12px}

.side-label{position:absolute;display:flex;flex-direction:column;align-items:center}
.side-label .label-title{writing-mode:vertical-rl;font-family:"Bebas Neue",sans-serif;font-size:28px;color:var(--brand-green);line-height:1;letter-spacing:.5px}
.side-label .label-rule{width:1px;background:var(--brand-green-line);margin:12px 0}
.side-label .label-motto{writing-mode:vertical-rl;font-size:9px;color:var(--ink)}
.page--front .side-label{left:26px;top:329px}
.page--front .label-rule{height:82px}
.page--back .side-label{left:27px;top:34px}
.page--back .label-rule{height:308px}

.services{position:absolute;left:71px;display:flex;flex-direction:column;gap:12px}
.page--front .services{top:331px;width:448px}
.page--back .services{top:34px;width:447px}
.service{height:102px;background:var(--card-bg);border-radius:6px;display:flex;overflow:hidden}
.service-photo{width:154px;flex:none;border-radius:6px}
.service-body{flex:1;display:flex;flex-direction:column;justify-content:center;padding:4px 12px 4px 17px}
.service-title{font-family:"Bebas Neue",sans-serif;font-weight:400;font-size:19px;line-height:1;color:var(--ink);letter-spacing:.4px;margin-bottom:5px}
.service-text{font-size:6.9px;line-height:10.6px}
.service-text p+p{margin-top:10px}
.service-text a{color:var(--brand-green);text-decoration:none;font-weight:500}

.photo-track{background:linear-gradient(150deg,#6c8f9b,#3f9a45 45%,#2d2d35 75%,#a63a35)}
.photo-grass{background:linear-gradient(180deg,#5d8fd0 0%,#9dc0e6 40%,#6f9a3e 60%,#7fae44 100%)}
.photo-turf{background:linear-gradient(180deg,#9fb7c9 0%,#5a8f3c 35%,#4d4d4d 65%,#9c9a94 100%)}
.photo-stadium{background:linear-gradient(160deg,#8ea38c,#c9c8c3 40%,#4f8c3f 60%,#a58a72)}
.photo-tennis{background:linear-gradient(180deg,#5fa4e6 0%,#2f5e30 35%,#2c63b9 60%,#4c9a3e 100%)}
.photo-repair{background:linear-gradient(180deg,#b7c3c8 0%,#3b7a35 25%,#336d2f 100%)}
.photo-lighting{background:linear-gradient(90deg,#6b7a4b 0%,#8a9a5c 48%,#1e2a1c 52%,#58a04a 100%)}
.photo-maintenance{background:linear-gradient(180deg,#a9c2d8 0%,#3f8e43 35%,#7c3a9a 70%,#6a2f86 100%)}

.footer{position:absolute;left:25px;top:611px;width:492px;height:56px;display:flex;align-items:center}
.footer .brand-lockup{width:151px;display:flex;flex-direction:column;align-items:center}
.contact{flex:1;height:56px;background:var(--dark-panel);border-radius:8px;color:#fff;
  display:grid;grid-template-columns:1fr auto;align-content:center;row-gap:7px;padding:0 16px 0 10px;font-size:7.2px}
.contact-item{display:flex;align-items:center;gap:5px;white-space:nowrap}
.contact-item svg{width:9px;height:9px;flex:none}
.contact-phone{font-size:10px;font-weight:600}
</style>
</head>
<body>

<section class="page page--front">
  <div class="hero" role="img" aria-label="Aerial photo of a stadium field under construction with gravel piles and a bulldozer"></div>
  <div class="brand-box">
    <span class="brand-name">Brindle</span>
    <span class="brand-tag">Sports Construction</span>
  </div>

  <div class="intro">
    <h1 class="intro-title">Turnkey<br>Solutions for<br>Sports<br>Construction</h1>
    <div class="intro-rule"></div>
    <div class="intro-copy">
      <p>Brindle Sports Construction offers turnkey solutions in the realm of general sports construction. We're committed to excellence in all we do, and we seek to develop lasting relationships with our clients. Brindle is not in the business to win a single job and move on. We are working to earn your trust and business as we want you as a customer for life.</p>
      <p>At Brindle we have 7 Proverbs we strive to live by. Our #1 proverb is to <strong>“Deliver On Our Promises”</strong>. That is our promise to you that we will strive to deliver on time with the quality and service you expect and deserve on every job.</p>
    </div>
  </div>

  <div class="side-label">
    <span class="label-title">Our Services</span>
    <span class="label-rule"></span>
    <span class="label-motto">Deliver On Our Promises</span>
  </div>

  <div class="services">
    <article class="service">
      <div class="service-photo photo-track" role="img" aria-label="Aerial photo of a turf football field ringed by a running track"></div>
      <div class="service-body">
        <h2 class="service-title">Track Construction</h2>
        <div class="service-text"><p>Brindle recommends the Stridelane line of running track systems developed by Corvane Athletic, owned by Fieldwell Group, as the industry leaders in high quality, performance-enhancing systems that result in unmatched results for the lifecycle of your track.</p></div>
      </div>
    </article>
    <article class="service">
      <div class="service-photo photo-grass" role="img" aria-label="Photo of a natural grass baseball field under blue sky"></div>
      <div class="service-body">
        <h2 class="service-title">Natural Grass Fields</h2>
        <div class="service-text"><p>Natural Grass is a growing area of our business and we have brought in natural grass experts to join the Brindle team who understand the challenges involved with installing and maintaining grass fields. Two of our experts are certified field builders with one specializing in both synthetic and natural grass installations.</p></div>
      </div>
    </article>
    <article class="service">
      <div class="service-photo photo-turf" role="img" aria-label="Photo of workers installing synthetic turf with a seaming machine"></div>
      <div class="service-body">
        <h2 class="service-title">Synthetic Turf Field Construction</h2>
        <div class="service-text">
          <p>With the wide selection of synthetic turf systems– no matter the venue or sport - Brindle has a viable solution.</p>
          <p>Verdacoat's premium turf system series boasts heavy face weights for the best the industry has to offer in aesthetics, durability, and player protection.</p>
        </div>
      </div>
    </article>
  </div>
</section>

<section class="page page--back">
  <div class="side-label">
    <span class="label-title">Our Services</span>
    <span class="label-rule"></span>
    <span class="label-motto">Deliver On Our Promises</span>
  </div>

  <div class="services">
    <article class="service">
      <div class="service-photo photo-stadium" role="img" aria-label="Aerial photo of a finished stadium with stands and turf field"></div>
      <div class="service-body">
        <h2 class="service-title">Stadium Construction</h2>
        <div class="service-text"><p>In every sense of the word, Brindle is a one-stop shop for all things sports construction. We are a true turn-key construction company owned and operated by seasoned professionals who care. From ground-up stadium construction to total lifecycle planning, we provide custom construction solutions through all stages of your projects.</p></div>
      </div>
    </article>
    <article class="service">
      <div class="service-photo photo-tennis" role="img" aria-label="Photo of blue and green tennis courts lined with pine trees"></div>
      <div class="service-body">
        <h2 class="service-title">Tennis Court Construction</h2>
        <div class="service-text"><p>To ensure that our customers are playing on the best tennis courts available, we've partnered with Corvane Athletic to provide Courtline court surfacing systems. Courtline offers a variety of impact reducing, performance enhancing court systems that are of the highest quality in the industry.</p></div>
      </div>
    </article>
    <article class="service">
      <div class="service-photo photo-repair" role="img" aria-label="Photo of a worker in a hard hat inspecting synthetic turf"></div>
      <div class="service-body">
        <h2 class="service-title">Repair and Maintenance</h2>
        <div class="service-text"><p>Brindle Sports is here to support you throughout the entire lifecycle of your sports construction projects from conception to intermittent servicing when needed. We provide maintenance services and support for all sports surfaces, helping you protect your investment and extend the life of your synthetic turf, track or tennis court through education, performance testing, and maintenance services.</p></div>
      </div>
    </article>
    <article class="service">
      <div class="service-photo photo-lighting" role="img" aria-label="Before and after aerial photos of a field under old and new LED lighting"></div>
      <div class="service-body">
        <h2 class="service-title">Stadium Lighting</h2>
        <div class="service-text"><p>Brindle also provides lighting services. Take advantage of the energy efficiency and cost savings by converting to LED lighting. According to the National Energy Bureau, light-emitting diodes (LED) are six to seven times more energy efficient than conventional light bulbs and cut energy use by more than 80 percent.</p></div>
      </div>
    </article>
    <article class="service">
      <div class="service-photo photo-maintenance" role="img" aria-label="Photo of a ride-on groomer maintaining a purple and green turf field"></div>
      <div class="service-body">
        <h2 class="service-title">Maintenance Programs</h2>
        <div class="service-text"><p>All sports systems involve some component of maintenance to ensure your surface is performing properly and will withstand the test of time. Many of our synthetic fields undergo annual field maintenance and bacterial and COVID killing sprays. If you would like to have a free maintenance or field/surface evaluation, please email us at <a href="mailto:aftercare@brindlesports.example">aftercare@brindlesports.example</a>.</p></div>
      </div>
    </article>
  </div>

  <footer class="footer">
    <div class="brand-lockup">
      <span class="brand-name">Brindle</span>
      <span class="brand-tag">Sports Construction</span>
    </div>
    <div class="contact">
      <span class="contact-item contact-phone">
        <svg viewBox="0 0 24 24" fill="none" stroke="#6fb07f" stroke-width="2"><path d="M5 3h4l2 5-3 2a12 12 0 0 0 6 6l2-3 5 2v4a2 2 0 0 1-2 2A17 17 0 0 1 3 5a2 2 0 0 1 2-2z"/></svg>
        (555) 014 2290
      </span>
      <span class="contact-item">
        <svg viewBox="0 0 24 24" fill="none" stroke="#6fb07f" stroke-width="2"><rect x="3" y="5" width="18" height="14" rx="1"/><path d="M3 6l9 7 9-7"/></svg>
        info@brindlesports.example
      </span>
      <span class="contact-item">
        <svg viewBox="0 0 24 24" fill="none" stroke="#6fb07f" stroke-width="2"><path d="M12 22s7-7 7-12a7 7 0 0 0-14 0c0 5 7 12 7 12z"/><circle cx="12" cy="10" r="2.5"/></svg>
        48 Harlan Street, Cedar Hollow, Texas 75000
      </span>
      <span class="contact-item">
        <svg viewBox="0 0 24 24" fill="none" stroke="#6fb07f" stroke-width="2"><circle cx="12" cy="12" r="9"/><path d="M3 12h18M12 3c3 3 3 15 0 18M12 3c-3 3-3 15 0 18"/></svg>
        www.brindlesports.example
      </span>
    </div>
  </footer>
</section>

</body>
</html>
```